Offshore Energy Projects Management Consultancy needs a business card design

Logo available. We provide teams to deliver engineering consultancy, project management and delivery teams mainly in the offshore renewables sector. The company is all about bringing the right people to a project to deliver the scope.

The business card will be used for all staff.

The business card should be quite simple, vibrant and uncluttered but convey experience, enthusiasm and integration.

Target Market(s)

Energy Project Developers and Tier 1 construction companies

Contact Information for Business Card

Logo should be on the back of the card. I'm happy for the designer to play with the colour of the logo and background colour.

Front of the card should convey all the must have information in a clear and professional manner but without being overly traditional.

Colors

Designer to choose colors to be used in the design.

Requirements
Must have
• Land Line Tel Number, Mobile Tel Number, Email, business address, web address.

```html
<!DOCTYPE html>
<html lang="en">
<head>
<meta charset="utf-8">
<title>Tidewater Delivery Group – Business Card</title>
<link href="https://fonts.googleapis.com/css2?family=Rubik:wght@300;400;500;600&display=swap" rel="stylesheet">
<style>
  :root {
    --page-bg: #ffffff;
    --card-light: #f2f2f3;
    --brand-blue: #1174bd;
    --accent-blue: #2a9be0;
    --ink-grey: #5f6062;
    --text-dark: #3a3a3c;
    --rule: #6b6b6d;
    --white: #ffffff;
  }
  html, body {
    margin: 0;
    padding: 0;
    width: 902px;
    height: 1200px;
    overflow: hidden;
    background: var(--page-bg);
    font-family: "Rubik", Arial, sans-serif;
  }
  .canvas { position: relative; width: 902px; height: 1200px; }

  .card {
    position: absolute;
    left: 78px;
    width: 745px;
    height: 437px;
    border-radius: 20px;
    overflow: hidden;
  }
  .card--front { top: 132px; background: var(--card-light); }
  .card--back { top: 637px; background: var(--brand-blue); }

  /* front */
  .brand-name {
    position: absolute;
    left: 0; right: 0;
    text-align: center;
    font-weight: 500;
    text-transform: uppercase;
    margin: 0;
  }
  .card--front .brand-name {
    top: 136px;
    font-size: 21px;
    letter-spacing: 0.5px;
    color: var(--ink-grey);
  }
  .brand-dot {
    position: absolute;
    left: 340px;
    top: 78px;
    width: 50px;
    height: 50px;
    border-radius: 50%;
    background: var(--brand-blue);
  }
  .divider {
    position: absolute;
    left: 67px;
    top: 211px;
    width: 612px;
    height: 1px;
    background: var(--rule);
  }
  .person {
    position: absolute;
    right: 414px;
    top: 232px;
    text-align: right;
    white-space: nowrap;
  }
  .person__name {
    margin: 0;
    font-size: 30px;
    font-weight: 400;
    color: var(--brand-blue);
    line-height: 34px;
  }
  .person__name .surname { color: var(--accent-blue); }
  .person__role {
    margin: 4px 0 0;
    font-size: 18px;
    color: var(--text-dark);
    line-height: 22px;
  }
  .person__address {
    margin: 9px 0 0;
    font-size: 18px;
    font-weight: 300;
    font-style: normal;
    color: var(--brand-blue);
    line-height: 22px;
  }
  .contacts {
    position: absolute;
    left: 430px;
    top: 240px;
    margin: 0;
    padding: 0;
    list-style: none;
  }
  .contacts li {
    display: flex;
    align-items: center;
    height: 22px;
    font-size: 17.5px;
    color: var(--text-dark);
  }
  .contacts svg {
    width: 14px;
    height: 14px;
    margin-right: 13px;
    fill: var(--brand-blue);
    flex: none;
  }

  /* back */
  .card--back .brand-name {
    top: 196px;
    font-size: 38px;
    letter-spacing: 1px;
    color: var(--white);
  }
</style>
</head>
<body>
<main class="canvas">

  <section class="card card--front" aria-label="Card front">
    <span class="brand-dot" aria-hidden="true"></span>
    <p class="brand-name">Tidewater Delivery Group</p>
    <div class="divider"></div>

    <div class="person">
      <h1 class="person__name">Jonas <span class="surname">Whitfield</span></h1>
      <p class="person__role">CEO/ Founder</p>
      <address class="person__address">12th floor, Harbour Road no<br>48 Quay Tower</address>
    </div>

    <ul class="contacts">
      <li>
        <svg viewBox="0 0 24 24" aria-hidden="true"><path d="M6.6 10.8a15.1 15.1 0 0 0 6.6 6.6l2.2-2.2a1 1 0 0 1 1-.25 11.4 11.4 0 0 0 3.6.57 1 1 0 0 1 1 1V20a1 1 0 0 1-1 1A17 17 0 0 1 3 4a1 1 0 0 1 1-1h3.5a1 1 0 0 1 1 1c0 1.25.2 2.45.57 3.57a1 1 0 0 1-.25 1z"/></svg>
        +44 7700 900412
      </li>
      <li>
        <svg viewBox="0 0 24 24" aria-hidden="true"><path d="M2 9c0-3 4.5-5 10-5s10 2 10 5v1.5h-5V8H7v2.5H2zM6 11h12l3 9H3zm6 2.5a2.5 2.5 0 1 0 0 5 2.5 2.5 0 0 0 0-5z"/></svg>
        +44 20 7946 0321
      </li>
      <li>
        <svg viewBox="0 0 24 24" aria-hidden="true"><path d="M2 5h20v14H2zm2 2v.5l8 5.5 8-5.5V7zm0 2.9V17h16V9.9l-8 5.5z"/></svg>
        jonas@tidewaterdg.com
      </li>
      <li>
        <svg viewBox="0 0 24 24" aria-hidden="true"><path d="M12 2a10 10 0 1 0 0 20 10 10 0 0 0 0-20zm-1 17.9A8 8 0 0 1 4.1 11H7l2 2v2l2 2zm6.9-2.6L16 15h-2v-3h-4V9h2l2-3h2.5a8 8 0 0 1 1.4 11.3z"/></svg>
        www.tidewaterdg.com
      </li>
    </ul>
  </section>

  <section class="card card--back" aria-label="Card back">
    <p class="brand-name">Tidewater Delivery Group</p>
  </section>

</main>
</body>
</html>
```